Brand design for Corvanel Holdings

We are a new start up Fund Manager based in Singapore in need of a stylish and slick corporate identity starting with letterhead and business card (2 separate projects on pixel bazaar but must be completed as one). We are aiming to be a somewhat 'budget' service provider with a target market of high net worth individuals and savvy self traders so we need to have our look convey value but with style. Our logo is attached and the use of the blue is imperative. The company name is Corvanel Holdings Pte Ltd and the verbiage 'Licensed by the Treasury Conduct Bureau of Singapore - QTLD licence no. XQZ908172-3' should be incorporated in small print.

Business card should also include address, office, direct and mobile numbers as well as email address. Follow me on blabber/pk/workloop/Zentro+ should also be incrorporated. We are also looking to have a QR code on the business card that people can read with a smartphone which will auto populate our contact details in to their address book.

Many thanks and happy designing!

Reason: Extending so we can have further internal discussions. Thanks for input so far, some great designs coming through! Cheers

```html
<!DOCTYPE html>
<html lang="en">
<head>
<meta charset="utf-8">
<title>Corvanel Holdings – Letterhead</title>
<link rel="stylesheet" href="https://fonts.googleapis.com/css2?family=Arimo:wght@400;700&family=Roboto:wght@400&display=swap">
<style>
  :root {
    --brand-blue: #0a4ea2;
    --band-blue: #0b7bc1;
    --ink: #2b2b2b;
    --ink-soft: #6a6a6a;
    --paper: #ffffff;
    --rule-dark: #7a7a7a;
    --rule-light: #d8d8d8;
  }
  * { margin: 0; padding: 0; box-sizing: border-box; }
  html, body { width: 928px; height: 1200px; overflow: hidden; background: var(--paper); }
  .letterhead {
    position: relative;
    width: 928px;
    height: 1200px;
    background: var(--paper);
    font-family: "Arimo", Arial, sans-serif;
    color: var(--ink);
  }
  .top-rule {
    position: absolute; top: 0; left: 0; width: 928px; height: 1px;
    background: linear-gradient(to right, var(--rule-dark) 0 258px, var(--rule-light) 258px 100%);
  }
  .brand {
    position: absolute; top: 66px; right: 86px;
    display: flex; align-items: center; gap: 10px;
    color: var(--brand-blue);
    font-family: "Arimo", Arial, sans-serif;
    font-weight: 700; font-size: 38px; letter-spacing: 0.5px;
  }
  .brand-mark { width: 14px; height: 14px; background: var(--brand-blue); }
  .salutation {
    position: absolute; top: 288px; left: 254px;
    font-size: 14px; font-weight: 700; color: var(--ink-soft);
  }
  .letter-body {
    position: absolute; top: 325px; left: 254px; width: 540px;
    font-size: 11px; line-height: 20px; color: var(--ink);
  }
  .letter-body p + p { margin-top: 20px; }
  .closing {
    position: absolute; top: 921px; left: 254px;
    font-size: 11px; color: var(--ink-soft);
  }
  .footer-band {
    position: absolute; left: 0; top: 1097px; width: 928px; height: 103px;
    background: var(--band-blue);
    color: #fff; text-align: center;
    font-family: "Roboto", Arial, sans-serif;
    padding-top: 16px;
  }
  .footer-address { font-size: 14.5px; line-height: 20px; }
  .footer-contact { font-size: 16.5px; line-height: 21px; }
  .footer-licence { font-size: 12px; line-height: 15px; }
</style>
</head>
<body>
<main class="letterhead">
  <div class="top-rule"></div>

  <header class="brand">
    <span class="brand-mark"></span>
    <span class="brand-name">CORVANEL.COM</span>
  </header>

  <h1 class="salutation">Dear Mr. Harlow</h1>

  <section class="letter-body">
    <p>Lorem ipsum dolor sit amet, consectetur adipiscing elit. Vestibulum adipiscing felis ac tortor consectetur<br>
    feugiat. Etiam malesuada sodales eros ut ornare. Sed lorem eros, mattis id pretium ut, faucibus sit amet<br>
    quam. Nullam consectetur ultricies ipsum, fringilla porttitor erat ornare at. Sed sit amet dui vel sapien ultrices<br>
    vulputate. In hac habitasse platea dictumst. Nam est nisi, rhoncus at sagittis a, porttitor adipiscing nulla.<br>
    Vivamus placerat felis ultrices quam iaculis eget dignissim felis egestas. Integer nec molestie lorem. Sed odio<br>
    tellus, vulputate sed laoreet non, vulputate id justo. Etiam suscipit, odio vel auctor dictum, felis turpis ullamcor-<br>
    per neque, quis sodales risus metus in magna. Morbi pellentesque justo et quam laoreet facilisis. Aenean<br>
    placerat, urna ornare aliquet tincidunt, lorem justo molestie ligula, id placerat est metus nec lectus. Nullam eu<br>
    ipsum quis turpis tristique iaculis rutrum nec nibh. Phasellus risus eros, semper sit amet faucibus sit amet,<br>
    laoreet et neque. Donec eros sem, viverra dictum faucibus quis, ullamcorper tincidunt nulla.</p>
    <p>Aenean ut congue tellus. Class aptent taciti sociosqu ad litora torquent per conubia nostra, per inceptos hime-<br>
    naeos. Sed facilisis, velit tincidunt pharetra fermentum, urna tortor iaculis erat, vitae sollicitudin leo mauris quis<br>
    mi. Cras malesuada sem ac ipsum sagittis ultrices. Mauris fermentum porttitor nisi, eu facilisis lorem consecte-<br>
    tur et. Suspendisse est elit, scelerisque ac euismod id, scelerisque viverra odio. Nullam scelerisque metus in<br>
    eros semper congue. Fusce a fermentum est. Ut ac leo dolor. Quisque dignissim mauris a neque luctus<br>
    pretium ultrices risus sagittis. Aenean quam massa, rutrum ac hendrerit eu, interdum eu nulla. Curabitur a velit<br>
    mauris, sed porta eros. Cras id egestas sapien. Proin non metus eget felis eleifend adipiscing. Nunc male-<br>
    suada pharetra blandit.</p>
  </section>

  <p class="closing">Your sincerely</p>

  <footer class="footer-band">
    <p class="footer-address">Corvanel Holdings Pte Ltd, Level 27 Harbourline Exchange Tower 1, 48 Quayfront Avenue, Singapore 049372</p>
    <p class="footer-contact">(555) 014 238 690, info@corvanel.com</p>
    <p class="footer-licence">Licensed by the Treasury Conduct Bureau of Singapore - QTLD licence no. XQZ908172-3</p>
  </footer>
</main>
</body>
</html>
```